Tennly Packaging Business Card

Project Overview
We are seeking a modern, minimalist business card that effectively represents our company while making a bold and lasting impression. The design should reflect trust, professionalism, and innovation, reinforcing our expertise in custom plastic manufacturing for warehouse and distribution centers.

Provided Assets & Specifications
Logo: We will provide our official logo for integration into the design.
Design Files: Photoshop (PSD) files for our printing specifications will be supplied.

Card Size & Material:
Dimensions: 3.5" x 2"
Material: 1/8" Radius Plastic Business Cards with 1/8" Rounded Corners
Clear plastic background—the design should strategically incorporate transparency.
Orientation: The card should be designed in landscape format for a sleek and professional presentation.

Design Requirements:
Logo Prominence
The logo must be the focal point of the card.
Space should be used effectively to draw attention to the logo while maintaining a minimalist layout.

Clear Plastic Integration
The transparent background should create the illusion of blank space, enhancing the modern and high-quality feel.
Avoid any frosted effects—we do not want white areas to appear semi-transparent.

Minimalist & Impactful
Clean, structured, and easy to read at a glance.
Focus on sharp contrast to ensure legibility and visibility.
The design should instill confidence and reflect our role as a leading plastics manufacturer.

Color Palette & Contrast
Primary Colors: Blue, Black, White, and Grey
Use bold black or blue for text and key elements to ensure they stand out against the clear plastic.
Avoid light, pastel, or neon colors that may fade into the plastic background.
No frosted or semi-transparent white—we do not want a cloudy effect.

Typography & Information Hierarchy
Bold, modern typography—clear, professional, and highly legible.
The business card should highlight:
Company Logo (Primary Focus)
Full Name & Title
Phone Number
Email
Website

Brand Representation
The card should reflect our expertise in manufacturing high-quality custom plastics for large-scale packaging and distribution businesses.
Our clients rely on us to enhance their brand presence through custom plastic solutions, and our business cards should reinforce that sense of precision and trust.

Final Considerations
Utilize the clear plastic effectively to differentiate our brand from standard business cards.
Maintain a sleek, professional aesthetic while ensuring all text and elements remain legible.
The design should align with our industry, conveying reliability and innovation.
We look forward to seeing a design that captures our brand identity, maximizes the clear plastic medium, and makes a strong, professional impact on our clients.

```html
<!DOCTYPE html>
<html lang="en">
<head>
<meta charset="utf-8">
<title>Tennly Packaging Business Card</title>
<link href="https://fonts.googleapis.com/css2?family=Montserrat:wght@400;500;700;800&display=swap" rel="stylesheet">
<style>
  :root {
    --backdrop: #2e2f33;
    --card-dark: #333335;
    --card-light: #ffffff;
    --brand-blue: #1a88c2;
    --ink: #2b2b2d;
    --white: #ffffff;
  }
  * { box-sizing: border-box; margin: 0; padding: 0; }
  html, body { width: 1200px; height: 913px; overflow: hidden; }
  body {
    background: var(--backdrop);
    font-family: "Montserrat", sans-serif;
    position: relative;
  }
  .card {
    position: absolute;
    left: 280px;
    width: 640px;
    height: 366px;
    border-radius: 22px;
    box-shadow: 0 5px 0 var(--brand-blue), 0 14px 30px rgba(0,0,0,.45);
    overflow: hidden;
  }
  .card--front { top: 48px; background: var(--card-dark); }
  .card--back { top: 480px; background: var(--card-light); }

  .wordmark {
    position: absolute;
    display: flex;
    align-items: center;
    gap: 22px;
  }
  .wordmark__square { display: block; }
  .wordmark__name {
    font-weight: 700;
    line-height: 1.05;
    letter-spacing: 1px;
  }
  .card--front .wordmark { left: 92px; top: 118px; }
  .card--front .wordmark__name { color: var(--white); font-size: 50px; }
  .card--front .wordmark__rule {
    position: absolute; left: 130px; right: -20px; top: 198px;
    height: 4px; background: var(--brand-blue);
  }

  .card--back .wordmark { left: 48px; top: 140px; gap: 14px; }
  .card--back .wordmark__name { color: var(--ink); font-size: 27px; }

  .divider {
    position: absolute; left: 352px; top: 56px; width: 2px; height: 252px;
    background: var(--brand-blue);
  }
  .contact {
    position: absolute; left: 378px; top: 60px;
    color: var(--ink);
    font-size: 15px; line-height: 1.45; font-weight: 500;
  }
  .contact__name {
    color: var(--brand-blue);
    font-weight: 800; font-size: 25px; letter-spacing: .5px;
    line-height: 1.1;
  }
  .contact__title { margin-bottom: 12px; }
  .contact__address { margin-bottom: 10px; }
  .contact__row { display: flex; align-items: center; gap: 8px; }
  .contact__row svg { flex: none; }
</style>
</head>
<body>

  <section class="card card--front" aria-label="Card front">
    <div class="wordmark">
      <svg class="wordmark__square" width="92" height="92" viewBox="0 0 92 92" aria-hidden="true">
        <rect x="6" y="6" width="80" height="80" fill="none" stroke="var(--brand-blue)" stroke-width="9"/>
      </svg>
      <div class="wordmark__name">Tennly<br>Packaging</div>
    </div>
    <div class="wordmark__rule" style="left:206px; right:72px; top:250px;"></div>
  </section>

  <section class="card card--back" aria-label="Card back">
    <div class="wordmark">
      <svg class="wordmark__square" width="56" height="56" viewBox="0 0 56 56" aria-hidden="true">
        <rect x="4" y="4" width="48" height="48" fill="none" stroke="var(--brand-blue)" stroke-width="6"/>
      </svg>
      <div class="wordmark__name">Tennly<br>Packaging</div>
    </div>

    <div class="divider"></div>

    <div class="contact">
      <div class="contact__name">DANA KELLER</div>
      <div class="contact__title">Managing Director</div>
      <div class="contact__address">Your address, City<br>State, Zip 1234</div>
      <div class="contact__row">
        <svg width="14" height="14" viewBox="0 0 14 14" aria-hidden="true"><path d="M3 1 L5 1 L6 4 L4.5 5.2 C5.4 7 6.9 8.6 8.8 9.5 L10 8 L13 9 L13 11 C13 12 12 13 11 13 C5.5 13 1 8.5 1 3 C1 2 2 1 3 1 Z" fill="var(--brand-blue)"/></svg>
        <span>123 456 789</span>
      </div>
      <div class="contact__row">
        <svg width="14" height="14" viewBox="0 0 14 14" aria-hidden="true"><rect x="1" y="3" width="12" height="8" fill="var(--brand-blue)"/><path d="M1 3 L7 8 L13 3" fill="none" stroke="#fff" stroke-width="1.2"/></svg>
        <span>info@yourmail.com</span>
      </div>
      <div class="contact__row">
        <svg width="14" height="14" viewBox="0 0 14 14" aria-hidden="true"><circle cx="7" cy="7" r="6" fill="var(--brand-blue)"/><path d="M1 7 H13 M7 1 C4 4 4 10 7 13 M7 1 C10 4 10 10 7 13" fill="none" stroke="#fff" stroke-width="1"/></svg>
        <span>www.yourwebsite.com</span>
      </div>
    </div>
  </section>

</body>
</html>
```